Postcard to Market Greeting Cards

Need a Postcard to
* Promote a particular human being and his story.
* Market and raise awareness of his art
* Advertise his website where the art can be purchased.

Background:
Davor Kelmandi is a refugee and artist trapped in a refugee camp in Indonesia.
He has committed no crimes. He had to escape his country as a refugee.
He is currently held in detention. The only way out is to be privately sponsored.
This costs a huge amount of money. Davor is working to raise the money needed.
He is young and has lost 5 years being imprisoned. We must work to save him.

He draws everyday and sends the drawings to me. I make them into beautiful hand drawn art cards which we sell at markets, on the internet or via contacts.
He is not allowed to work. Secret drawing is the only way he can make a living.

This postcard is to
* share some of Davor's Story and to give a sense of who he is.
* display his beautiful art cards which are sold for income via his website.
* Prominently display his website address as well as images of the cards.

These postcards will be given out at markets, letterbox dropped, sent to new customers, left in cafes and libraries etc so people will discover Davor's Cards....
By buying the cards...Davor can earn the funds he needs to pay for sponsorship into a free country. Many countries will accept him if he pays for the process.

Therefore...the postcard needs to be filled front and back. No need to leave space for address and postage. This leaves more room for samples of the Greeting Cards.

There is text provided for the front and back of the POSTCARD.
This may be edited and added to as the design process continues.

Images of Davor's Cards have been uploaded for you.
It would be great if these can be beautifully and artistically presented on the postcard. The aim is to attract people to Davor's hand drawn cards motivate people to want to buy them. Not all of the card images need to be used.

There are * black line cards * colour cards. * framed colour art works
so some of each could be promoted on the postcard.

Davor's Story will be included on the back of the card labelled for the Back.
A few words will be clearly and displayed on the front. Labelled fo the front.

The front art can be a single drawing image from Davor OR a collage of many OR
It can contain his image or a few small images. See what you feel works well as there is scope to create a BEAUTIFUL postcard that depicts beautiful CARDS.

There is a quote from Davor to be included on the front.
Can it be written in a handwriting style font to make it look like Davor has written the message himself ?

There are images of Davor to be used on the front and back.
Davor's images have ben taken on dodgy phones and may not be a good quality.
They don't need to be large images and they DON'T need to all be used. There is a selection to choose from.

Davor is in a prison. Maybe there are design elements that might remind of this.
Barbed wire maybe. Fences. The over all feel though is FREEDOM and BEAUTY in the hand drawn art cards and the escape they will provide in the end.

Davor's website to be displayed on the front and back
davorsketch.net

email address on the back
helpdavor2031@mailpost.net

These postcards will encourage buyers to read Davor's Story and want to help.
They will display beautifully hand drawn art cards which people will want to buy.
They will display the website address prominently and in some clever. arty way.

Good luck with it all.
I plan to increase first prize money depending on the designs....
and to offer more than first place depending on the deigns.

Please feel free to ask me any questions at any time.

Good luck and thanks for considering this project.

Neil Farrow

Target Market(s)

Broad human rights supporters who will enjoy seeing a human story and will want to. respond.

Industry/Entity Type

Human Rights

Colors

Designer to choose colors to be used in the design.

Requirements
Must have
• Colourful and imaginative way of displaying the Greeting Cards being marketed by the Postcard. It is a taster and a sampling. They do not need to be arranged in rows or order..better to be creative in displaying the samples of cards. The website has the organised online shop. The postcard is a sampler and should MAKE people want to go to the website to buy the cards. The postcard must share the story of the artist.
• Handwriting font for the quote from the artist to make it look like he has written a personal message.
• Postcard needs to be filled on front and back. No blank space for mailing and address.
Nice to have
• Free and easy arty design. Photograph of the artist placed in some creative way.
Should not have
• Conservative structure. Free and arty is better.
• The postcard needs to be filled on the front and back ! No need to leave the bank area for mailing as it will only be used for marketing and distribution. it won't actually be used for mailing.

```html
<!DOCTYPE html>
<html lang="en">
<head>
<meta charset="utf-8">
<title>Davor's Cards – Postcard</title>
<link rel="stylesheet" href="https://fonts.googleapis.com/css2?family=Amatic+SC:wght@400;700&family=Dancing+Script:wght@700&family=Arvo&family=Vazirmatn:wght@300;400&display=swap">
<style>
  :root {
    --paper: #ffffff;
    --ink: #333333;
    --script-ink: #3a3a3a;
    --accent-orange: #e8825a;
    --accent-green: #5fa37c;
    --pencil-light: #ececec;
    --pencil-mid: #d6d6d6;
    --blush: #f3e2de;
    --blush-deep: #e9d2cc;
    --cream: #f8f0d6;
    --cream-deep: #f1e4bd;
    --petal: rgba(240, 140, 60, 0.55);
    --leaf: rgba(70, 140, 70, 0.40);
  }
  * { margin: 0; padding: 0; box-sizing: border-box; }
  html, body {
    width: 1200px; height: 930px; overflow: hidden;
    background: var(--paper);
  }
  .postcard {
    position: relative; width: 1200px; height: 930px;
    background: var(--paper); color: var(--ink);
    font-family: "Amatic SC", cursive;
  }
  .story {
    position: absolute; left: 46px;
    font-size: 24px; line-height: 28.8px; letter-spacing: 0.2px;
    text-transform: uppercase; white-space: nowrap;
  }
  .story span { display: block; }
  .story--intro { top: 40px; }
  .story--column { top: 210px; }
  .website {
    position: absolute; left: 52px; top: 796px;
    font-family: "Amatic SC", cursive; font-weight: 400;
    font-size: 76px; line-height: 80px; color: #111;
    text-transform: uppercase; white-space: nowrap;
  }
  .sketch, .colour-card { position: absolute; }
  .sketch {
    background: radial-gradient(ellipse at 50% 45%, var(--pencil-light) 0%, var(--pencil-mid) 100%);
    box-shadow: 0 1px 2px rgba(0,0,0,0.12);
  }
  .colour-card { box-shadow: 0 1px 2px rgba(0,0,0,0.1); }
  .colour-card--blush {
    background:
      radial-gradient(ellipse 55% 35% at 50% 40%, var(--petal), transparent 100%),
      radial-gradient(ellipse 60% 30% at 50% 78%, var(--leaf), transparent 100%),
      linear-gradient(180deg, var(--blush), var(--blush-deep));
  }
  .colour-card--cream {
    background:
      radial-gradient(ellipse 55% 35% at 50% 35%, var(--petal), transparent 100%),
      radial-gradient(ellipse 60% 28% at 50% 80%, var(--leaf), transparent 100%),
      linear-gradient(180deg, var(--cream), var(--cream-deep));
  }
  .caption {
    position: absolute; width: 190px; text-align: center;
    transform: translateX(-50%);
  }
  .caption__word {
    display: block;
    font-family: "Dancing Script", cursive; font-weight: 700;
    font-size: 54px; line-height: 58px; color: var(--script-ink);
  }
  .caption__farsi {
    display: block;
    font-family: "Vazirmatn", sans-serif; font-weight: 300;
    font-size: 26px; line-height: 44px; color: var(--script-ink);
  }
  .tag {
    position: absolute; width: 180px; text-align: center;
    transform: translateX(-50%);
  }
  .tag__en {
    display: block; font-family: "Arvo", serif;
    font-size: 22px; line-height: 26px; color: var(--accent-orange);
    letter-spacing: 0.5px;
  }
  .tag__farsi {
    display: block; font-family: "Vazirmatn", sans-serif;
    font-size: 15px; line-height: 28px; color: var(--accent-green);
  }
</style>
</head>
<body>
<main class="postcard">
  <section class="story story--intro">
    <span>Davor Kelmandi, a young Hazara man from Afghanistan, has been illegally held captive in an Indonesian detention centre for</span>
    <span>more than four years.</span>
    <span>He is a refugee and prisoner without any crime. The Hazara are a ruthlessly persecuted people. Davor is alone in the world and</span>
    <span>bravely escaped his country to begin a new free life never expecting to be imprisoned and detained for years.</span>
    <span>An artist and photographer Davor is now a passionate human rights defender. He refuses to allow his free spirit and creative</span>
    <span>nature to be dampened or imprisoned. He draws sunny delicate flowers and peaceful fragile birds which sing of freedom.</span>
  </section>
  <section class="story story--column">
    <span>Davor makes his art to maintain his sanity and to en-</span>
    <span>courage all who struggle for freedom to reach out</span>
    <span>and grab it with both hands. He draws daily to remind</span>
    <span>himself that what is important</span>
    <span>inside him can never be locked away. Davor wastes no</span>
    <span>time being a prisoner. He is too busy dreaming free. His</span>
    <span>art expresses that.</span>
    <span>The only escape for Davor is to be sponsored to a free</span>
    <span>country. It costs many thousands to be sponsored.</span>
    <span>Davor needs your help. He's not asking for favours or</span>
    <span>charity. He is working daily for this.</span>
    <span>Davor's daily drawings have become individual greeting</span>
    <span>cards and</span>
    <span>his beautiful, unique cards are now for sale to fund</span>
    <span>his freedom.</span>
    <span>Buy Davor's greeting cards so he can pay his own way</span>
    <span>to freedom. Individual cards. Sets of cards. Stunning</span>
    <span>framed art works. Beautiful black line drawing cards</span>
    <span>and full colour cards available.</span>
    <span>Davor's cards, art and designs are available from</span>
  </section>
  <div class="website">www.davorsketch.net</div>

  <div class="sketch" style="left:443px;top:250px;width:171px;height:168px" role="img" aria-label="Pencil drawing card: a bird perched on a tree stump"></div>
  <div class="sketch" style="left:634px;top:250px;width:172px;height:168px" role="img" aria-label="Pencil drawing card: a crested bird on a branch"></div>
  <div class="sketch" style="left:833px;top:250px;width:135px;height:168px" role="img" aria-label="Pencil drawing card: a small bird on a leafy twig"></div>
  <div class="sketch" style="left:994px;top:250px;width:135px;height:168px" role="img" aria-label="Pencil line drawing card: a flower cluster with a bud"></div>

  <div class="caption" style="left:528px;top:426px"><span class="caption__word">Be</span><span class="caption__farsi">بودن</span></div>
  <div class="caption" style="left:718px;top:426px"><span class="caption__word">Gentle</span><span class="caption__farsi">آرام</span></div>
  <div class="caption" style="left:898px;top:426px"><span class="caption__word">Still</span><span class="caption__farsi">هنوز</span></div>
  <div class="caption" style="left:1062px;top:426px"><span class="caption__word">Bloom</span><span class="caption__farsi">شکوفه</span></div>

  <div class="tag" style="left:544px;top:553px"><span class="tag__en">BE PEACE</span><span class="tag__farsi">صلح‌باش</span></div>
  <div class="tag" style="left:718px;top:553px"><span class="tag__en">BE PEACE</span><span class="tag__farsi">صلح‌باش</span></div>
  <div class="tag" style="left:891px;top:553px"><span class="tag__en">BE HOPE</span><span class="tag__farsi">امیدوارباش</span></div>
  <div class="tag" style="left:1064px;top:553px"><span class="tag__en">BE HOPE</span><span class="tag__farsi">امیدوارباش</span></div>

  <div class="colour-card colour-card--blush" style="left:468px;top:610px;width:154px;height:204px" role="img" aria-label="Colour card: bouquet of orange flowers with green leaves on a blush background"></div>
  <div class="colour-card colour-card--blush" style="left:641px;top:610px;width:154px;height:204px" role="img" aria-label="Colour card: bouquet of orange flowers with green leaves on a blush background"></div>
  <div class="colour-card colour-card--cream" style="left:814px;top:608px;width:154px;height:206px" role="img" aria-label="Colour card: two orange lilies with green leaves on a cream background"></div>
  <div class="colour-card colour-card--cream" style="left:987px;top:608px;width:154px;height:206px" role="img" aria-label="Colour card: two orange lilies with green leaves on a cream background"></div>
</main>
</body>
</html>
```